Title: “The Lantern Path, Rebuilding The Spirit of Harbors, A Sailor’s Journal”

Cover design for ebook and printable book. Looking for this specific designer

```html
<!DOCTYPE html>
<html lang="en">
<head>
<meta charset="UTF-8">
<title>The Lantern Path — Book Cover</title>
<link href="https://fonts.googleapis.com/css2?family=Cinzel:wght@400;600&display=swap" rel="stylesheet">
<style>
  :root {
    --paper: #ffffff;
    --ink: #050505;
    --accent: #bb170c;
  }
  * { margin: 0; padding: 0; box-sizing: border-box; }
  html, body { width: 761px; height: 1200px; overflow: hidden; background: var(--paper); }
  .cover {
    position: relative;
    width: 761px;
    height: 1200px;
    overflow: hidden;
    background: var(--paper);
    color: var(--ink);
    font-family: "Cinzel", "Trajan Pro", serif;
    text-align: center;
    text-transform: uppercase;
  }
  .cover > * { position: absolute; left: 0; width: 100%; white-space: nowrap; }
  .subtitle {
    top: 34px;
    font-size: 42px;
    font-weight: 400;
    line-height: 55px;
    letter-spacing: 2px;
  }
  .tagline {
    top: 153px;
    font-size: 25px;
    font-weight: 600;
    line-height: 30px;
    letter-spacing: 2px;
    color: var(--accent);
  }
  .title {
    top: 198px;
    font-size: 112px;
    font-weight: 400;
    line-height: 134px;
    letter-spacing: 0;
  }
  .title span { display: block; }
  .illustration {
    top: 636px;
    left: 200px;
    width: 360px;
    height: 392px;
  }
  .author {
    top: 1100px;
    font-size: 54px;
    font-weight: 400;
    line-height: 66px;
    letter-spacing: 16px;
    padding-left: 16px;
  }
</style>
</head>
<body>
  <main class="cover">
    <h2 class="subtitle">Rebuilding the Spirit<br>of Harbors</h2>
    <p class="tagline">A Sailor's Journal</p>
    <h1 class="title"><span>The</span><span>Lantern</span><span>Path</span></h1>
    <svg class="illustration" viewBox="0 0 360 392" role="img" aria-label="Illustration of a red anatomical heart cradled in two outlined hands">
      <defs>
        <radialGradient id="heart-glow" cx="50%" cy="50%" r="50%">
          <stop offset="0%" stop-color="#bb170c"/>
          <stop offset="50%" stop-color="#bb170c" stop-opacity="0.9"/>
          <stop offset="80%" stop-color="#bb170c" stop-opacity="0.35"/>
          <stop offset="100%" stop-color="#bb170c" stop-opacity="0"/>
        </radialGradient>
      </defs>
      <ellipse cx="180" cy="196" rx="180" ry="196" fill="url(#heart-glow)"/>
    </svg>
    <p class="author">Author Name</p>
  </main>
</body>
</html>
```